Criação de Papelaria Profissional para Imóveis
A empresa queria:
" Eu sou conhecido no seguimento . Atuo no meio e alto padrão. Vendo Para as construtoras e revendas . Lotes e casas "

```html
<!DOCTYPE html>
<html lang="pt-BR">
<head>
<meta charset="utf-8">
<title>Cartão de Visita – Vallore</title>
<link rel="stylesheet" href="https://fonts.googleapis.com/css2?family=Montserrat:wght@400;500;600;700;800&display=swap">
<style>
  :root{
    --bg-light:#ececed;
    --bg-dark:#c9c9cb;
    --navy:#0b2442;
    --navy-deep:#06182e;
    --navy-light:#163a63;
    --gold:#c9a05a;
    --gold-dark:#8e6631;
    --text:#17233a;
    --muted:#3c4656;
    --white:#ffffff;
  }
  *{margin:0;padding:0;box-sizing:border-box}
  html,body{width:1200px;height:1200px;overflow:hidden}
  body{
    position:relative;
    font-family:"Montserrat",sans-serif;
    background:linear-gradient(135deg,var(--bg-light) 0%,var(--bg-light) 55%,var(--bg-dark) 55%,var(--bg-dark) 100%);
  }
  .page-title{
    position:absolute;top:48px;left:0;width:100%;
    text-align:center;font-size:38px;font-weight:700;letter-spacing:3px;color:var(--navy);
  }
  .card{
    position:absolute;left:233px;width:732px;border-radius:26px;overflow:hidden;
    box-shadow:0 10px 26px rgba(0,0,0,.25);
  }
  .card-front{
    top:156px;height:420px;
    background:radial-gradient(ellipse at 20% 15%,var(--navy-light) 0%,var(--navy) 45%,var(--navy-deep) 100%);
  }
  .front-accent{
    position:absolute;right:-40px;bottom:-40px;width:300px;height:300px;
    background:rgba(255,255,255,.05);
  }
  .brand{display:flex;align-items:center;justify-content:center;gap:18px}
  .brand-square{background:var(--gold)}
  .brand-name{font-weight:800;color:var(--gold);letter-spacing:4px}
  .card-front .brand{position:absolute;top:0;left:0;width:100%;height:100%}
  .card-front .brand-square{width:46px;height:46px}
  .card-front .brand-name{font-size:74px}

  .card-back{top:631px;height:425px;background:var(--white)}
  .name-row{
    position:absolute;top:52px;left:0;width:100%;
    display:flex;align-items:center;justify-content:space-between;
  }
  .rule{height:5px;width:200px;background:linear-gradient(90deg,var(--gold-dark),var(--gold))}
  .rule-right{background:linear-gradient(90deg,var(--gold),var(--gold-dark))}
  .person-name{font-size:28px;font-weight:700;color:var(--text)}
  .person-role{position:absolute;top:97px;width:100%;text-align:center;font-size:19px;color:var(--muted)}
  .card-back .brand{position:absolute;top:148px;left:0;width:100%}
  .card-back .brand-square{width:30px;height:30px}
  .card-back .brand-name{font-size:50px}

  .contact{position:absolute;display:flex;gap:12px;color:var(--text);font-size:19px;font-weight:500;line-height:1.3}
  .contact svg{flex:none;width:22px;height:22px;margin-top:2px}
  .contact-phone{left:70px;top:270px}
  .contact-address{left:70px;top:340px}
  .contact-email{left:400px;top:282px}
  .contact-social{left:400px;top:342px}
</style>
</head>
<body>
  <h1 class="page-title">CARTÃO DE VISITA</h1>

  <section class="card card-front">
    <div class="front-accent"></div>
    <div class="brand">
      <span class="brand-square"></span>
      <span class="brand-name">VALLORE</span>
    </div>
  </section>

  <section class="card card-back">
    <div class="name-row">
      <span class="rule"></span>
      <span class="person-name">Nome e Sobrenome</span>
      <span class="rule rule-right"></span>
    </div>
    <p class="person-role">Diretor Comercial</p>
    <div class="brand">
      <span class="brand-square"></span>
      <span class="brand-name">VALLORE</span>
    </div>

    <div class="contact contact-phone">
      <svg viewBox="0 0 24 24" fill="none" stroke="var(--gold)" stroke-width="2"><path d="M5 3h4l2 5-3 2a12 12 0 0 0 6 6l2-3 5 2v4a2 2 0 0 1-2 2A18 18 0 0 1 3 5a2 2 0 0 1 2-2z"/></svg>
      <span>(99) 90412-3378<br>(99) 90587-2260</span>
    </div>
    <div class="contact contact-address">
      <svg viewBox="0 0 24 24" fill="none" stroke="var(--gold)" stroke-width="2"><path d="M12 22s7-7 7-12a7 7 0 0 0-14 0c0 5 7 12 7 12z"/><circle cx="12" cy="10" r="2.5"/></svg>
      <span>Av. das Acácias, 880 - Centro<br>Cidade/UF - CEP: 12345-678</span>
    </div>
    <div class="contact contact-email">
      <svg viewBox="0 0 24 24" fill="none" stroke="var(--gold)" stroke-width="2"><rect x="3" y="5" width="18" height="14" rx="2"/><path d="M3 7l9 6 9-6"/></svg>
      <span>valloreimoveis@email.com</span>
    </div>
    <div class="contact contact-social">
      <svg viewBox="0 0 24 24" fill="none" stroke="var(--gold)" stroke-width="2"><circle cx="12" cy="12" r="9"/></svg>
      <span>@valloreimoveis</span>
    </div>
  </section>
</body>
</html>
```